Lena Harcourt Tennis Academy - New Website

Our business is built around classes for all ages, competitions, and court hire.

There are a few gym style Wordpress templates that I think will have most of the functionality we need, but we don't like the style. We are looking for someone to make us a design that can be implemented as a child theme to one of these gym based Wordpress themes.

We have looked at:

http://plinthmarket.example/item/active-studio-responsive-wordpress-theme/full_screen_preview/7318264?ref=BrixoPages
http://www.vardel-skins.example/item/gym-fitness/demo/?r=brixopages
http://www.drumo.example/redirect/?theme=movewell

For style we are looking for something fresh, clean, and vibrant. Our logo is teal and gold with some red, orange, green and yellow.

https://huewheel.example/Citrus-Dawn-color-theme-738415/
https://huewheel.example/Mint-Frost-color-theme-604927/
https://huewheel.example/Solvane-color-theme-83051/

These are the colour schemes we are leaning towards.

Our current website can be seen here www.lhta-courts.example
Updates

The new logo design will be uploaded shortly. We don't need any more work done on that.

A rough logo file has been added for you to work with.

Could I please get some submissions that include what the other pages on the website will look like (instead of just the home page).

I think it's really important that we get the look of the product page. See the design pdf for our ideas on the layout of those pages.

***Edit*** Single product pages, I mean. I think the "Classes" page itself will be based a lot on the theme used so I'm less concerned about that. I just want to see what a page will look like that is only for.... Twilight Rally (for example)

Target Market(s)

We teach a lot of kids but also many comp players. Everything needs to be very clear and easy to navigate.

Industry/Entity Type

Court

Requirements
Must have
• Custom content types to easily post new things (eg, new programs, new coaches)
Timetable page that is dynamic based on the programs custom type.
Programs page that is dynamic based on the programs custom type.
Coaches page that is dynamic based on the coaches/trainers content type.

Page templates for programs, competitions and a few other things as per pdf.

```html
<!DOCTYPE html>
<html lang="en">
<head>
<meta charset="utf-8">
<title>Lena Harcourt Tennis Academy</title>
<link rel="stylesheet" href="https://fonts.googleapis.com/css2?family=Montserrat:wght@600&family=Open+Sans:wght@400;600;700&family=Bree+Serif&family=Pacifico&family=Oswald:wght@500&display=swap">
<style>
:root{
  --teal:#2fa9b8;
  --teal-strip:#3ab8c6;
  --cream:#fdf1dd;
  --orange:#f26b0f;
  --orange-light:#f9a62a;
  --gold:#f7b52a;
  --brown:#983a1f;
  --ink:#333;
  --grey-bg:#f2f2f2;
  --card-border:#a9a9a9;
}
*{box-sizing:border-box;margin:0;padding:0}
html,body{width:959px;height:1200px;overflow:hidden}
body{position:relative;background:#fff;font-family:"Open Sans",Arial,sans-serif;color:var(--ink)}

.site-header{position:absolute;left:0;top:0;width:959px;height:167px;background:var(--cream);border-top:4px solid var(--teal-strip)}
.brand{position:absolute;left:120px;top:20px;font-family:"Montserrat",Arial,sans-serif;font-weight:600;color:var(--teal);line-height:1}
.brand .name{font-size:27px;letter-spacing:.5px}
.brand .sub{font-size:19px;letter-spacing:3.5px;margin-top:6px;padding-left:10px}
.top-links{position:absolute;left:633px;top:42px;font-size:12px;color:var(--ink)}
.top-links span{margin-right:9px}
.social{position:absolute;top:36px;width:26px;height:26px;border-radius:50%;background:var(--orange);box-shadow:0 1px 2px rgba(0,0,0,.25)}

.main-nav{position:absolute;left:120px;top:100px;width:719px;height:46px;border-radius:3px;background:linear-gradient(#6d6d6d,#3d3d3d);padding:4px;box-shadow:0 6px 6px -3px rgba(0,0,0,.35)}
.main-nav ul{display:flex;list-style:none;height:38px;background:linear-gradient(#fdfdfd,#e6e6e6 60%,#d9d9d9)}
.main-nav li{font-size:13px;color:#222;display:flex;align-items:center;justify-content:center;border-right:1px solid #bdbdbd;border-left:1px solid #fff}
.main-nav li:last-child{border-right:none}

.hero{position:absolute;left:0;top:167px;width:959px;height:370px;background:linear-gradient(100deg,#7f8b6a 0%,#9aa37f 22%,#d7a7b8 38%,#c25a86 48%,#4a4a48 62%,#2d2f2e 80%,#5d6158 100%)}
.intro-card{position:absolute;left:667px;top:366px;width:164px;height:172px;background:rgba(255,255,255,.88);text-align:center;padding:6px 14px}
.intro-card h2{font-weight:400;font-size:21px;color:var(--teal-strip);margin-bottom:6px}
.intro-card p{font-size:9.5px;line-height:15px;color:#888}
.slider-arrows{position:absolute;left:667px;top:538px;width:164px;height:23px;display:flex}
.slider-arrows div{flex:1;display:flex;align-items:center;justify-content:center}

.promo{position:absolute;left:127px;top:576px;width:704px;height:114px;background:radial-gradient(ellipse at 55% 50%,#b04a28,var(--brown) 70%)}
.promo .frame{position:absolute;inset:5px;border:1px dashed rgba(255,215,170,.55)}
.promo h3{position:absolute;left:24px;top:24px;font-family:"Pacifico",cursive;font-weight:400;font-size:28px;color:var(--gold);line-height:1.2}
.promo p{position:absolute;left:97px;top:68px;font-size:14px;color:#fff}
.promo .photo{position:absolute;left:345px;top:0;width:150px;height:114px;background:linear-gradient(90deg,rgba(152,58,31,0),#c8885e 45%,#3c4a6a 70%,rgba(152,58,31,0))}
.book-btn{position:absolute;left:537px;top:42px;width:137px;height:30px;border-radius:4px;background:linear-gradient(#f98a3a,#e25d10);box-shadow:0 2px 0 #7a2a0d;color:#fff;font-family:"Oswald",sans-serif;font-weight:500;font-size:14px;display:flex;align-items:center;justify-content:center;letter-spacing:.3px}
.dots{position:absolute;left:459px;top:699px;display:flex;gap:3px}
.dots i{width:5px;height:5px;border-radius:50%;background:#ddd}
.dots i:first-child{background:#9fd9e0}

.widgets{position:absolute;left:0;top:727px;width:959px;height:345px;background:var(--grey-bg)}
.card{position:absolute;top:750px;width:224px;height:282px;background:#fff;border:3px solid var(--card-border);border-radius:5px;box-shadow:0 3px 4px rgba(0,0,0,.12)}
.card-title{position:absolute;left:8px;top:9px;width:202px;height:38px;border-radius:3px;background:linear-gradient(var(--orange-light),#f08a12);color:#fff;font-family:"Bree Serif",serif;font-weight:400;font-size:20px;padding-left:11px;line-height:38px;box-shadow:0 2px 2px rgba(0,0,0,.2)}
.learn-more{position:absolute;left:62px;top:259px;width:95px;height:30px;background:linear-gradient(#f07a2a,#d9520f);border:2px solid #c9c9c9;color:#fff;font-size:11px;display:flex;align-items:center;justify-content:center;clip-path:polygon(8% 0,92% 0,100% 50%,92% 100%,8% 100%,0 50%)}
.player-photo{position:absolute;left:11px;top:66px;width:197px;height:134px;border:3px solid #fff;outline:1px solid #ccc;background:linear-gradient(135deg,#f0e0c8,#c9a27e 40%,#5d7fa6 75%,#e3e7ea)}
.player-name{position:absolute;left:16px;top:208px;font-weight:700;font-size:16px;color:#333;letter-spacing:-.2px}
.post{position:absolute;left:8px;width:204px}
.post h4{font-size:11.5px;font-weight:600;color:#222}
.post .meta{font-size:8px;color:#999;margin-top:1px}
.post .meta b{color:var(--orange);font-weight:400}
.post .thumb{position:absolute;left:0;top:33px;width:51px;height:51px;border:1px solid #ddd;background:#fff}
.post .excerpt{position:absolute;left:63px;top:31px;font-size:8.5px;line-height:12px;color:#777;width:130px}
.post .excerpt b{color:var(--orange);font-weight:400}
.event{position:absolute;left:10px;width:200px;height:60px;border-bottom:1px solid #e6e6e6}
.event .date{position:absolute;left:2px;top:0;width:42px;height:42px;border-radius:50%;background:var(--teal-strip);border:3px solid #dff2f4;color:#fff;text-align:center;font-weight:700;line-height:1}
.event .date small{display:block;font-size:7.5px;margin-top:6px}
.event .date span{font-size:17px}
.event p{position:absolute;left:53px;width:140px;font-size:11px;font-weight:600;color:#222;line-height:12.5px}

.site-footer{position:absolute;left:0;top:1072px;width:959px;height:128px;background:var(--teal);color:#fff}
.contact{position:absolute;top:17px;font-size:10px;line-height:13px}
.contact b{font-weight:700}
.newsletter{position:absolute;left:600px;top:13px}
.newsletter h5{font-family:"Oswald",sans-serif;font-weight:500;font-size:15px}
.newsletter .field{display:flex;margin-top:4px}
.newsletter .input{width:160px;height:19px;background:#fff;color:#333;font-size:9px;padding:4px 6px}
.newsletter .btn{width:70px;height:19px;background:var(--orange);font-size:10px;font-weight:700;display:flex;align-items:center;justify-content:center}
.footer-rule{position:absolute;left:120px;top:68px;width:720px;height:1px;background:rgba(255,255,255,.25)}
.footer-nav{position:absolute;left:0;top:80px;width:959px;text-align:center;font-size:10px;font-weight:600}
.footer-nav span{margin:0 7px}
.copyright{position:absolute;left:0;top:102px;width:959px;text-align:center;font-size:10px}
</style>
</head>
<body>

<header class="site-header">
  <div class="brand">
    <div class="name">LENA HARCOURT</div>
    <div class="sub">TENNIS ACADEMY</div>
  </div>
  <nav class="top-links"><span>Home</span><span>Conatct Us</span></nav>
  <div class="social" style="left:747px"></div>
  <div class="social" style="left:780px"></div>
  <div class="social" style="left:813px"></div>
  <nav class="main-nav">
    <ul>
      <li style="width:94px">Programs</li>
      <li style="width:105px">Competitions</li>
      <li style="width:90px">Court Hire</li>
      <li style="width:82px">Restrings</li>
      <li style="width:70px">Gallery</li>
      <li style="width:82px">Schedule</li>
      <li style="width:55px">Blog</li>
      <li style="width:63px">About</li>
      <li style="width:70px">News</li>
    </ul>
  </nav>
</header>

<section class="hero" role="img" aria-label="Photo of a smiling young girl holding a tennis racket beside a tennis net"></section>
<aside class="intro-card">
  <h2>Who we are</h2>
  <p>Lorem Ipsum. Proin gravida nibh vel velit auctor aliquet. Aenean sollicitudin, lorem quis bibendum auctor, nisi elit consequat ipsum, nec sagittis sem nibh id elit. Duis sed odio sit amet nibh vulputate cursus a sit amet mauris.</p>
</aside>
<div class="slider-arrows">
  <div style="background:var(--gold)"><svg width="24" height="8"><path d="M1 4H23M1 4L5 1M1 4L5 7" stroke="#fff" fill="none"/></svg></div>
  <div style="background:var(--orange)"><svg width="24" height="8"><path d="M1 4H23M23 4L19 1M23 4L19 7" stroke="#fff" fill="none"/></svg></div>
</div>

<section class="promo">
  <div class="frame"></div>
  <h3>Summer Holiday Camps</h3>
  <p>Secure your childs place!</p>
  <div class="photo" role="img" aria-label="Photo of a young boy swinging a tennis racket at a ball"></div>
  <div class="book-btn">BOOK ONLINE NOW</div>
</section>
<div class="dots"><i></i><i></i><i></i><i></i><i></i></div>

<section class="widgets"></section>

<article class="card" style="left:127px">
  <h3 class="card-title">Player of the Month</h3>
  <div class="player-photo" role="img" aria-label="Photo of the player of the month with a coach and a friend"></div>
  <div class="player-name">Oliver Pryce June 2013</div>
  <div class="learn-more">LEARN MORE</div>
</article>

<article class="card" style="left:367px">
  <h3 class="card-title">Recent Post</h3>
  <div class="post" style="top:61px">
    <h4>Rain Make Ups Term 3-2013</h4>
    <div class="meta">Posted by <b>marcus</b> - Aug 15, 2013</div>
    <div class="thumb"><svg width="49" height="49"><ellipse cx="25" cy="22" rx="15" ry="9" fill="#5aa3d8"/><circle cx="19" cy="18" r="7" fill="#5aa3d8"/><circle cx="29" cy="16" r="8" fill="#5aa3d8"/><path d="M16 33l-2 5M22 33l-2 5M28 33l-2 5M34 33l-2 5" stroke="#3b86c4" stroke-width="2"/></svg></div>
    <p class="excerpt">Thursday Mini Rallies – Sunday 18th August @ 2pm. Friday Junior Elite – Sunday 18th August @ 3pm. <b>Read more...</b></p>
  </div>
  <div class="post" style="top:162px">
    <h4>Holler for a Hoodie Winners</h4>
    <div class="meta">Posted by <b>marcus</b> - Aug 1, 2013</div>
    <div class="thumb" role="img" aria-label="Thumbnail of a red hoodie" style="background:linear-gradient(#e8f3e0,#d9423a 60%,#f3f3f3)"></div>
    <p class="excerpt">We have a gone a little crazy and have selected 9 winners (instead of just 3) who will all receive a free. <b>Read more...</b></p>
  </div>
  <div class="learn-more">LEARN MORE</div>
</article>

<article class="card" style="left:607px">
  <h3 class="card-title">Upcoming Events</h3>
  <div class="event" style="top:60px"><div class="date"><small>AUG</small><span>26</span></div><p style="top:16px">Coastal Open 2013</p></div>
  <div class="event" style="top:127px"><div class="date"><small>SEP</small><span>08</span></div><p style="top:5px">8:00 AM RJTA Comp T3-2013 @ LHTA Elmwood (Home Matches)</p></div>
  <div class="event" style="top:193px;border-bottom:none"><div class="date"><small>SEP</small><span>15</span></div><p style="top:5px">8:00 AM RJTA Comp T3-2013 @ LHTA Elmwood (Home Matches)</p></div>
  <div class="learn-more">LEARN MORE</div>
</article>

<footer class="site-footer">
  <div class="contact" style="left:120px"><svg width="10" height="13" style="position:absolute;left:0;top:0"><path d="M5 12C2 8 1 6 1 4.5a4 4 0 018 0C9 6 8 8 5 12z" fill="#cdeef2"/><circle cx="5" cy="4.5" r="1.5" fill="#2fa9b8"/></svg><div style="padding-left:16px"><b>LHTA PTY LTD</b><br>48 Banksia Grove Rd,<br>Elmwood NSW 2190.</div></div>
  <div class="contact" style="left:285px"><svg width="10" height="13" style="position:absolute;left:0;top:0"><path d="M3 1l2 3-1.5 1.5c.5 1.5 2 3 3.5 3.5L8.5 7.5l1.5 2.5-2 2C4 11 1 6 1 2z" fill="#cdeef2"/></svg><div style="padding-left:14px"><b>Phone:</b><br>+(02) 5550-1842</div></div>
  <div class="contact" style="left:415px"><svg width="13" height="10" style="position:absolute;left:0;top:2px"><rect x=".5" y=".5" width="12" height="8" fill="#cdeef2"/><path d="M.5.5l6 4.5 6-4.5" stroke="#2fa9b8" fill="none"/></svg><div style="padding-left:16px"><b>Email:</b><br>info@lhta-courts.example</div></div>
  <div class="newsletter">
    <h5>NEWSLETTER</h5>
    <div class="field"><div class="input">Enter your email address</div><div class="btn">SUBSCRIBE</div></div>
  </div>
  <div class="footer-rule"></div>
  <nav class="footer-nav"><span>Home</span><span>Programs</span><span>Competitions</span><span>Court Hire</span><span>Restrings</span><span>Gallery</span><span>Schedule</span><span>Blog</span><span>About</span><span>News</span><span>Contact Us</span></nav>
  <div class="copyright">Copyright © 2013 LHTA PTY LTD. All rights reserved.</div>
</footer>

</body>
</html>
```